Thai Restruant Business Card Design

A Business card design for a Thai and Laos take away restaurant.

We are a highly respectable take away restaurant in a small shopping center.

The design must have a Papaya Tree and Thai Palace.

The final design should communicate, innovation, fun and delicious food.

Industry/Entity Type

Restaurant

Contact Information for Business Card

Mango Hearth, Thai & Lao Food, Shop 4. 71 Elm Lane. Cabramatta N.S.W 2166, Tel. 02-96415270, Open 7 Days From 8.30am To 6.30pm

```html
<!DOCTYPE html>
<html lang="en">
<head>
<meta charset="utf-8">
<title>Mango Hearth – Business Card</title>
<link rel="stylesheet" href="https://fonts.googleapis.com/css2?family=UnifrakturMaguntia&family=Oswald:wght@400&family=Oranienbaum&display=swap">
<style>
  :root {
    --backdrop: #e9e7e4;
    --card: #ffffff;
    --ink: #111111;
    --frame: #222222;
    --band: #9b9b9b;
    --band-text: #ffffff;
    --art-light: #d6d6d6;
    --art-dark: #2a2a2a;
  }
  * { margin: 0; padding: 0; box-sizing: border-box; }
  html, body {
    width: 1200px;
    height: 1000px;
    overflow: hidden;
    background: var(--backdrop);
  }
  .business-card {
    position: absolute;
    left: 50px;
    top: 152px;
    width: 1100px;
    height: 697px;
    background: var(--card);
    box-shadow: 0 6px 24px rgba(0,0,0,0.12);
  }
  .card-frame {
    position: absolute;
    inset: 20px;
    border: 2px solid var(--frame);
  }
  .phone {
    position: absolute;
    top: 28px;
    right: 28px;
    font-family: "Oranienbaum", serif;
    font-size: 31px;
    color: var(--ink);
  }
  .brand-art {
    position: absolute;
    left: 329px;
    top: 102px;
    width: 432px;
    height: 146px;
    display: block;
  }
  .brand-name {
    position: absolute;
    left: 0;
    right: 0;
    top: 258px;
    text-align: center;
    font-family: "UnifrakturMaguntia", serif;
    font-size: 60px;
    font-weight: 400;
    color: var(--ink);
    line-height: 1;
  }
  .cuisine {
    position: absolute;
    left: 0;
    right: 0;
    top: 362px;
    text-align: center;
    font-family: "UnifrakturMaguntia", serif;
    font-size: 74px;
    color: var(--ink);
    line-height: 1;
  }
  .hours-band {
    position: absolute;
    left: 267px;
    top: 459px;
    width: 574px;
    height: 81px;
    background: var(--band);
    display: flex;
    align-items: center;
    justify-content: center;
    font-family: "Oswald", sans-serif;
    font-size: 25px;
    color: var(--band-text);
    letter-spacing: -0.5px;
  }
  .address {
    position: absolute;
    left: 0;
    right: 0;
    top: 618px;
    text-align: center;
    font-family: "Oranienbaum", serif;
    font-size: 33px;
    color: var(--ink);
  }
</style>
</head>
<body>
  <div class="business-card">
    <div class="card-frame"></div>
    <div class="phone">Tel. 02-96415270</div>

    <svg class="brand-art" viewBox="0 0 432 146" role="img" aria-label="Illustration of papaya trees flanking a Thai palace silhouette">
      <defs>
        <linearGradient id="art-fill" x1="0" y1="0" x2="0" y2="1">
          <stop offset="0" stop-color="var(--art-light)"/>
          <stop offset="1" stop-color="var(--art-dark)"/>
        </linearGradient>
      </defs>
      <rect x="0" y="0" width="432" height="146" fill="url(#art-fill)"/>
    </svg>

    <div class="brand-name">Mango Hearth</div>
    <div class="cuisine">Thai &amp; Lao Food</div>
    <div class="hours-band">Open 7 Days From 8.30am To 6.30pm</div>
    <div class="address">Shop 4. 71 Elm Lane. Cabramatta N.S.W 2166</div>
  </div>
</body>
</html>
```